Flyer Design for an electrical and security company trying to build local customers

I need a flyer design for a new company based in Sans Souci, Sydney 2219 called "Harbor Quill Dune Electrical and Security" also "HQD Electrical and Security". We are electrical contractors who are looking for more local work including emergency service calls and any project work including renovations or new constructions in the local area. I would like everyone in the area to know I am new and that I am available 24 hours a day 7 days a week. I would like to see designs that use the logo colours. Would also like the font of the entire design to be "juice bold".

Electrical

• juice bold

Requirements
Must have
• Must use the colours of the original logo and also have the information from the rear of the card. Must also have services buttons like the website picture attached.

```html
<!DOCTYPE html>
<html lang="en">
<head>
<meta charset="utf-8">
<title>Harbor Quill Dune Electrical and Security – Flyer</title>
<link href="https://fonts.googleapis.com/css2?family=Dosis:wght@400;500;600;700&display=swap" rel="stylesheet">
<style>
  :root {
    --brand-blue: #39b1e4;
    --brand-orange: #f47b3a;
    --brand-peach: #f9c3a2;
    --ink: #2f2f2f;
    --ink-soft: #4a4a4a;
    --footer-grey: #4b4b4b;
    --paper: #ffffff;
    --stage: #ffffff;
  }
  * { box-sizing: border-box; margin: 0; padding: 0; }
  html, body { width: 979px; height: 1200px; overflow: hidden; background: var(--stage); }
  body { font-family: "Dosis", sans-serif; color: var(--ink); }

  .flyer { position: relative; width: 979px; height: 1200px; background: var(--paper); overflow: hidden; }

  .hero-art { position: absolute; left: 0; top: 0; width: 979px; height: 600px; }

  .brand { position: absolute; left: 18px; top: 10px; }
  .brand-name {
    font-weight: 700; font-size: 36px; line-height: 30px; color: var(--ink-soft);
    text-transform: lowercase; letter-spacing: -0.5px;
  }
  .brand-tagline { font-weight: 700; font-size: 14px; color: var(--ink); margin-top: 6px; }

  .hero-message {
    position: absolute; left: 92px; top: 383px; width: 520px;
    font-weight: 600; font-size: 20px; line-height: 29px; color: #fff; letter-spacing: 0.6px;
  }

  .about { position: absolute; right: 26px; top: 536px; width: 540px; text-align: right; }
  .about-title { font-weight: 600; font-size: 22px; color: var(--ink-soft); }
  .about-title .accent-blue { color: var(--brand-blue); }
  .about-title .accent-orange { color: var(--brand-orange); }
  .about-text { font-size: 14px; line-height: 19px; color: var(--ink); margin-top: 6px; }

  .sectors { position: absolute; left: 88px; top: 588px; width: 240px; }
  .sectors-title { font-weight: 600; font-size: 24px; color: var(--ink-soft); text-align: center; }
  .sector-list { display: flex; justify-content: space-between; margin-top: 14px; list-style: none; }
  .sector { width: 76px; text-align: center; font-size: 11px; font-weight: 600; }
  .sector-icon { display: block; margin: 0 auto 6px; }

  .services { position: absolute; left: 22px; top: 730px; width: 935px; }
  .services-title { font-weight: 600; font-size: 24px; color: var(--ink-soft); text-align: center; }
  .service-grid {
    list-style: none; display: grid; grid-template-columns: repeat(5, 1fr);
    row-gap: 20px; margin-top: 22px;
  }
  .service { text-align: center; height: 112px; }
  .service-icon { display: block; margin: 0 auto 6px; }
  .service-name { font-weight: 600; font-size: 12px; color: var(--ink); }
  .service-blurb { font-size: 11px; line-height: 12px; color: var(--ink); width: 120px; margin: 8px auto 0; font-weight: 500; }

  .footer-bar {
    position: absolute; left: 0; bottom: 0; width: 979px; height: 36px;
    background: var(--footer-grey); color: #fff; font-weight: 600; font-size: 17px;
    display: flex; justify-content: center; align-items: center; gap: 60px; letter-spacing: 0.4px;
  }
</style>
</head>
<body>
<main class="flyer">

  <svg class="hero-art" viewBox="0 0 979 600" aria-hidden="false">
    <defs>
      <linearGradient id="interior-tones" x1="0" y1="1" x2="1" y2="0">
        <stop offset="0" stop-color="#3b2417"/>
        <stop offset="0.35" stop-color="#6b4a34"/>
        <stop offset="0.6" stop-color="#c9c2b8"/>
        <stop offset="1" stop-color="#f1f0ec"/>
      </linearGradient>
      <linearGradient id="peach-fade" x1="0" y1="0" x2="1" y2="0">
        <stop offset="0" stop-color="#f9c3a2" stop-opacity="0"/>
        <stop offset="1" stop-color="#f9c3a2"/>
      </linearGradient>
    </defs>
    <path class="hero-swoosh" fill="var(--brand-blue)"
      d="M0,150 Q160,70 430,30 L560,28 Q230,90 60,235 L55,520 Q320,560 979,500 L979,528 Q420,595 0,560 Z"/>
    <path class="hero-photo" role="img"
      aria-label="Photo of a smiling woman giving two thumbs up in a bright, modern renovated home interior with timber floors and indoor plants"
      fill="url(#interior-tones)"
      d="M60,235 Q230,90 560,28 L979,28 L979,500 Q320,560 55,520 Z"/>
    <path class="hero-peach-band" fill="url(#peach-fade)"
      d="M380,560 Q700,545 979,505 L979,540 Q700,585 380,580 Z"/>
    <path class="hero-orange-line" fill="none" stroke="var(--brand-orange)" stroke-width="4"
      d="M0,572 Q480,610 979,528"/>
  </svg>

  <header class="brand">
    <div class="brand-name">harbor<br>quill<br>dune</div>
    <div class="brand-tagline">electrical and security</div>
  </header>

  <p class="hero-message">We Do All House Renovations, Construction, Commercial, 24 Hour Emergency Services, New Installations, Repairs, Maintenace, Home Theater And So On...</p>

  <section class="about">
    <h2 class="about-title">About <span class="accent-blue">Harbor Quill</span> <span class="accent-orange">Dune</span></h2>
    <p class="about-text">Lorem ipsum dolor sit amet, contectuer adipiscing elit, sed diam nmmy nibh euismod tincidunt ut laoreet dolore magna aliquam erat volutpat. Ut wisi enim ad minim veniam, quis nostrud exerci tation ullamcorper suscipit lobortis nisl ut aliquip modo consequat. Duis autem vel eum iriure dolor in hendrerit in vulputate velit esse mlie consequat, vel illum dolore eu feugiat nulla facilisis at vero eros et accumsan et iust odio dignissim qui blandit praesent luptatum zzril delenit augue duis dolore te feugait nulla facilisi.</p>
  </section>

  <section class="sectors">
    <h2 class="sectors-title">Sectors We Serve</h2>
    <ul class="sector-list">
      <li class="sector">
        <svg class="sector-icon" width="50" height="50" viewBox="0 0 50 50"><circle cx="25" cy="25" r="24" fill="var(--brand-orange)"/><path d="M13,26 L25,14 L37,26 M17,23 V36 H33 V23" fill="none" stroke="#fff" stroke-width="3" stroke-linejoin="round"/></svg>
        Residential
      </li>
      <li class="sector">
        <svg class="sector-icon" width="50" height="50" viewBox="0 0 50 50"><circle cx="25" cy="25" r="24" fill="var(--brand-orange)"/><rect x="17" y="12" width="16" height="25" fill="#fff"/><path d="M21,16h2M27,16h2M21,21h2M27,21h2M21,26h2M27,26h2" stroke="var(--brand-orange)" stroke-width="2.5"/></svg>
        Commercial
      </li>
      <li class="sector">
        <svg class="sector-icon" width="50" height="50" viewBox="0 0 50 50"><circle cx="25" cy="25" r="24" fill="var(--brand-orange)"/><path d="M12,37 V24 L20,29 V24 L28,29 V14 H34 V37 Z" fill="#fff"/></svg>
        Industrial
      </li>
    </ul>
  </section>

  <section class="services">
    <h2 class="services-title">Our Services</h2>
    <ul class="service-grid">
      <li class="service">
        <svg class="service-icon" width="44" height="44" viewBox="0 0 44 44"><circle cx="22" cy="22" r="20" fill="var(--brand-orange)"/><path d="M14,27 Q14,15 22,15 Q30,15 30,27 Z M12,30 H32" fill="none" stroke="#fff" stroke-width="2.5"/></svg>
        <div class="service-name">24 Hour Emergency Services</div>
        <p class="service-blurb">Call any time, day or night, we come</p>
      </li>
      <li class="service">
        <svg class="service-icon" width="44" height="44" viewBox="0 0 44 44"><circle cx="22" cy="22" r="20" fill="none" stroke="var(--ink)" stroke-width="2"/><path d="M14,14 L30,30 M30,14 L14,30" stroke="var(--ink)" stroke-width="3" stroke-linecap="round"/></svg>
        <div class="service-name">New Installations</div>
        <p class="service-blurb">Wiring and fittings for every new build</p>
      </li>
      <li class="service">
        <svg class="service-icon" width="44" height="44" viewBox="0 0 44 44"><circle cx="22" cy="22" r="20" fill="none" stroke="var(--ink)" stroke-width="2"/><path d="M13,23 L22,14 L31,23 M16,21 V30 H28 V21" fill="none" stroke="var(--ink)" stroke-width="2"/></svg>
        <div class="service-name">Repairs</div>
        <p class="service-blurb">Faults found and fixed quickly and safely</p>
      </li>
      <li class="service">
        <svg class="service-icon" width="44" height="44" viewBox="0 0 44 44"><circle cx="22" cy="22" r="20" fill="none" stroke="var(--ink)" stroke-width="2"/><circle cx="22" cy="22" r="6" fill="none" stroke="var(--ink)" stroke-width="3"/><path d="M22,11v4M22,29v4M11,22h4M29,22h4" stroke="var(--ink)" stroke-width="3"/></svg>
        <div class="service-name">Maintenance</div>
        <p class="service-blurb">Regular checks keep your system running well</p>
      </li>
      <li class="service">
        <svg class="service-icon" width="44" height="44" viewBox="0 0 44 44"><circle cx="22" cy="22" r="20" fill="none" stroke="var(--ink)" stroke-width="2"/><path d="M12,23 L22,13 L32,23 H29 V31 H15 V23 Z" fill="var(--ink)"/></svg>
        <div class="service-name">Renovations/Extensions</div>
        <p class="service-blurb">Power planned for new rooms and extensions</p>
      </li>

      <li class="service">
        <svg class="service-icon" width="44" height="44" viewBox="0 0 44 44"><circle cx="22" cy="22" r="20" fill="none" stroke="var(--ink)" stroke-width="2"/><path d="M22,12 V32 M14,16 L30,28 M30,16 L14,28" stroke="var(--ink)" stroke-width="2"/></svg>
        <div class="service-name">Re-Wiring</div>
        <p class="service-blurb">Old cabling replaced to current safety standards</p>
      </li>
      <li class="service">
        <svg class="service-icon" width="44" height="44" viewBox="0 0 44 44"><circle cx="22" cy="22" r="20" fill="none" stroke="var(--ink)" stroke-width="2"/><rect x="13" y="15" width="18" height="12" rx="1" fill="none" stroke="var(--ink)" stroke-width="2.5"/><path d="M18,31 H26" stroke="var(--ink)" stroke-width="2.5"/></svg>
        <div class="service-name">Home Theatre</div>
        <p class="service-blurb">Screens and speakers set up for you</p>
      </li>
      <li class="service">
        <svg class="service-icon" width="44" height="44" viewBox="0 0 44 44"><circle cx="22" cy="22" r="20" fill="none" stroke="var(--ink)" stroke-width="2"/><rect x="12" y="16" width="8" height="13" fill="var(--ink)"/><rect x="24" y="16" width="8" height="13" fill="var(--ink)"/></svg>
        <div class="service-name">Surround Sound</div>
        <p class="service-blurb">Clear audio wired neatly through every room</p>
      </li>
      <li class="service">
        <svg class="service-icon" width="44" height="44" viewBox="0 0 44 44"><circle cx="22" cy="22" r="20" fill="none" stroke="var(--ink)" stroke-width="2"/><rect x="13" y="17" width="18" height="11" fill="none" stroke="var(--ink)" stroke-width="2"/><path d="M18,12 L22,17 L26,12" fill="none" stroke="var(--ink)" stroke-width="1.5"/></svg>
        <div class="service-name">Wall TV's</div>
        <p class="service-blurb">Televisions mounted level with cables fully hidden</p>
      </li>
      <li class="service">
        <svg class="service-icon" width="44" height="44" viewBox="0 0 44 44"><circle cx="22" cy="22" r="20" fill="none" stroke="var(--ink)" stroke-width="2"/><path d="M13,28 Q22,14 31,16" fill="none" stroke="var(--ink)" stroke-width="3" stroke-linecap="round"/><circle cx="13" cy="28" r="2.5" fill="var(--ink)"/></svg>
        <div class="service-name">Electric Hot Water</div>
        <p class="service-blurb">Hot water units installed and serviced fast</p>
      </li>

      <li class="service">
        <svg class="service-icon" width="44" height="44" viewBox="0 0 44 44"><circle cx="22" cy="22" r="20" fill="none" stroke="var(--ink)" stroke-width="2"/><rect x="14" y="14" width="16" height="17" rx="2" fill="none" stroke="var(--ink)" stroke-width="2.5"/><path d="M14,19 H30" stroke="var(--ink)" stroke-width="2"/></svg>
        <div class="service-name">Stoves</div>
        <p class="service-blurb">Stoves connected safely by licensed local electricians</p>
      </li>
      <li class="service">
        <svg class="service-icon" width="44" height="44" viewBox="0 0 44 44"><circle cx="22" cy="22" r="20" fill="none" stroke="var(--ink)" stroke-width="2"/><rect x="13" y="13" width="18" height="18" rx="3" fill="var(--ink)"/></svg>
        <div class="service-name">Cooktops</div>
        <p class="service-blurb">Cooktop installs and swaps done same week</p>
      </li>
      <li class="service">
        <svg class="service-icon" width="44" height="44" viewBox="0 0 44 44"><circle cx="22" cy="22" r="20" fill="none" stroke="var(--ink)" stroke-width="2"/><circle cx="22" cy="20" r="6" fill="none" stroke="var(--ink)" stroke-width="2.5"/><path d="M19,29 H25 M20,32 H24" stroke="var(--ink)" stroke-width="2"/></svg>
        <div class="service-name">Lighting &amp; Ceiling Fans</div>
        <p class="service-blurb">Lights and fans fitted to suit rooms</p>
      </li>
      <li class="service">
        <svg class="service-icon" width="44" height="44" viewBox="0 0 44 44"><circle cx="22" cy="22" r="20" fill="none" stroke="var(--ink)" stroke-width="2"/><path d="M12,19 Q22,11 32,19 L29,22 L26,19 H18 L15,22 Z" fill="var(--ink)"/><rect x="15" y="23" width="14" height="8" rx="2" fill="var(--ink)"/></svg>
        <div class="service-name">Telephone</div>
        <p class="service-blurb">Phone points added and lines tested properly</p>
      </li>
      <li class="service">
        <svg class="service-icon" width="44" height="44" viewBox="0 0 44 44"><circle cx="22" cy="22" r="20" fill="none" stroke="var(--ink)" stroke-width="2"/><path d="M22,12 L31,15 V22 Q31,29 22,33 Q13,29 13,22 V15 Z" fill="var(--ink)"/></svg>
        <div class="service-name">Security System</div>
        <p class="service-blurb">Alarms and cameras to protect your home</p>
      </li>
    </ul>
  </section>

  <footer class="footer-bar">
    <span class="footer-phone">Call Us Today 1300 555 214</span>
    <span class="footer-web">Visit HarborQuillDune.com</span>
  </footer>

</main>
</body>
</html>
```